Lawn mowing business card design

We need a business card design for our lawn mowing and gardening business which is located in the Northern Beaches of Sydney. Our business name is Meadowline Turf and our logo is predominantly green and yellow in color. Please see our website at www.meadowlineturf.com.au for design ideas. The business targets young professionals and older clientele. As such the font should be easy to read, but I also want the business card to be colorful and stand out.

Target Market(s)

young professionals

Industry/Entity Type

Lawn Care

Contact Information for Business Card

Meadowline Turf, Gareth Pellow, 0478559201, www.meadowlineturf.com.au, email: meadowlineturf@mailbox-example.com

Font styles to use
Serif

Colors
9bcb3b
fbed22

Requirements
Must have
• Must include the details listed above. Must include the attached logo.
Nice to have
• Logo attached with two copies. The logo without any writing is high quality, please feel free to be creative with the text stating our business name "Meadowline Turf" using this file.

```html
<!DOCTYPE html>
<html lang="en">
<head>
<meta charset="utf-8">
<title>Meadowline Turf – Business Card</title>
<link rel="stylesheet" href="https://fonts.googleapis.com/css2?family=Questrial&display=swap">
<style>
  :root {
    --backdrop: #d9dbd8;
    --card-white: #ffffff;
    --sky-top: #cfeaf8;
    --sky-low: #eaf6fb;
    --meadow-light: #a6dd3c;
    --meadow: #6cc126;
    --meadow-deep: #3d9a1a;
    --wave-pale: #d8f0a8;
    --wave-mid: #9bcb3b;
    --sun-yellow: #fbed22;
    --ink: #1e1e1e;
    --brand-ink: #2f6212;
  }
  * { margin: 0; padding: 0; box-sizing: border-box; }
  html, body {
    width: 1200px; height: 1200px; overflow: hidden;
    background: var(--backdrop);
    font-family: "Questrial", "Century Gothic", sans-serif;
  }
  .sheet {
    position: relative; width: 1200px; height: 1200px;
  }
  .card {
    position: absolute; left: 160px; width: 880px; height: 500px;
    background: var(--card-white); overflow: hidden;
  }
  .card--front { top: 60px; }
  .card--back { top: 640px; }
  .card svg { position: absolute; inset: 0; width: 100%; height: 100%; }

  .brand {
    position: absolute; display: flex; align-items: center;
    color: var(--brand-ink);
  }
  .brand__mark { background: var(--sun-yellow); flex: none; }
  .card--front .brand { top: 150px; right: 44px; gap: 10px; font-size: 24px; }
  .card--front .brand__mark { width: 18px; height: 18px; }
  .card--back .brand { top: 270px; left: 0; right: 0; justify-content: center; gap: 18px; font-size: 52px; }
  .card--back .brand__mark { width: 34px; height: 34px; }

  .contact {
    position: absolute; right: 60px; top: 345px; width: 420px;
    text-align: center; color: var(--ink);
  }
  .contact__name { font-size: 31px; letter-spacing: -0.5px; margin-left: 70px; }
  .contact__phone { font-size: 21px; letter-spacing: 0.5px; margin-left: 70px; }
  .contact__web { margin-top: 34px; font-size: 18px; line-height: 22px; letter-spacing: -0.3px; }
</style>
</head>
<body>
<main class="sheet">

  <section class="card card--front">
    <svg viewBox="0 0 880 500" preserveAspectRatio="none" aria-hidden="false">
      <defs>
        <linearGradient id="frontScene" x1="0" y1="0" x2="0" y2="1">
          <stop offset="0" stop-color="var(--sky-top)"/>
          <stop offset="0.28" stop-color="var(--sky-low)"/>
          <stop offset="0.42" stop-color="var(--meadow-light)"/>
          <stop offset="0.75" stop-color="var(--meadow)"/>
          <stop offset="1" stop-color="var(--meadow-deep)"/>
        </linearGradient>
      </defs>
      <rect role="img" aria-label="Illustrated green hill with bushes, tall grass and white and yellow flowers under a blue sky" x="0" y="0" width="880" height="500" fill="url(#frontScene)"/>
      <path class="wave wave--deep" d="M0 330 C 200 380, 420 300, 600 250 S 820 240, 880 240 L880 500 L0 500 Z" fill="var(--meadow-deep)"/>
      <path class="wave wave--mid" d="M0 365 C 230 420, 450 330, 620 275 S 830 255, 880 258 L880 500 L0 500 Z" fill="var(--wave-mid)"/>
      <path class="wave wave--pale" d="M0 410 C 240 450, 470 350, 640 290 S 840 268, 880 272 L880 500 L0 500 Z" fill="var(--wave-pale)"/>
      <path class="card-field" d="M0 440 C 250 470, 480 370, 660 305 S 850 280, 880 285 L880 500 L0 500 Z" fill="var(--card-white)"/>
    </svg>

    <div class="brand"><span class="brand__mark"></span><span class="brand__name">Meadowline Turf</span></div>

    <div class="contact">
      <p class="contact__name">Gareth Pellow</p>
      <p class="contact__phone">0478559201</p>
      <p class="contact__web">email: meadowlineturf@mailbox-example.com<br>www.meadowlineturf.com.au</p>
    </div>
  </section>

  <section class="card card--back">
    <svg viewBox="0 0 880 500" preserveAspectRatio="none">
      <defs>
        <linearGradient id="backScene" x1="0" y1="0" x2="0" y2="1">
          <stop offset="0" stop-color="var(--sky-top)"/>
          <stop offset="0.3" stop-color="var(--sky-low)"/>
          <stop offset="0.45" stop-color="var(--meadow-light)"/>
          <stop offset="0.8" stop-color="var(--meadow)"/>
          <stop offset="1" stop-color="var(--meadow-deep)"/>
        </linearGradient>
      </defs>
      <rect role="img" aria-label="Illustrated green hill with bushes, clouds, tall grass and white and yellow flowers" x="0" y="0" width="880" height="500" fill="url(#backScene)"/>
      <path class="wave wave--corner" d="M640 500 C 720 480, 820 460, 880 440 L880 500 Z" fill="var(--wave-pale)"/>
    </svg>

    <div class="brand"><span class="brand__mark"></span><span class="brand__name">Meadowline Turf</span></div>
  </section>

</main>
</body>
</html>
```